Wedding Invitation and Logo

We would like an invitation and logo designed for our wedding on October 19, 2019 in Charlotte, NC. Our names are Tessa and Boyd, we met in school at Kellridge Plains University, and we got engaged at a fire tower which has a view down to the campus. You do not have to include these, but some ideas for the invitation design would be mountains, a fire tower, our initials, or the city. The wedding will be at 4:30 in the afternoon with a reception to follow. We do not need to list the families as there are four of them and that is too much info. The colors we would like to use are white, black, royal blue, and maybe silver. Do not feel obligated to use them all though.We would like the logo to include similar elements such as mountains, fire tower, or our initials(T and B). The logo can be a one color design as we may use it on our cake, as light filters to be displayed on the walls at our reception, or as an accent on name plates and stationery.We like simple, clean designs and our wedding will have a wintery theme (white linens, white chair covers, silver and royal blue accents, etc.).Things we do not want: snowflakes, flowers, polka dots, leaves, gold foil.Thank you!

Font styles to use
Serif
Script

Requirements
Must have
• Some combination of white, black, royal blue, optionally silver.
Nice to have
• Mountains, fire tower, our initials (T and B), wintry theme (no snowflakes)
Should not have
• Snowflakes, flowers, polka dots, leaves, gold foil

```html
<!DOCTYPE html>
<html lang="en">
<head>
<meta charset="utf-8">
<title>Tessa and Boyd — Wedding Invitation</title>
<link rel="stylesheet" href="https://fonts.googleapis.com/css2?family=Playfair+Display:wght@700&family=Bodoni+Moda:wght@400&family=Cormorant+Garamond:wght@500&display=swap">
<style>
  :root {
    --backdrop: #e6e8ea;
    --card-white: #f7f7f7;
    --marble-grey: #dcdde0;
    --royal-blue: #2e2fa0;
    --ink: #111111;
    --card-shadow: rgba(0, 0, 0, 0.14);
  }
  * { margin: 0; padding: 0; box-sizing: border-box; }
  html, body {
    width: 1034px;
    height: 1200px;
    overflow: hidden;
    background: var(--backdrop);
  }
  .canvas {
    position: relative;
    width: 1034px;
    height: 1200px;
  }
  .invitation {
    position: absolute;
    left: 116px;
    top: 40px;
    width: 802px;
    height: 1120px;
    background: radial-gradient(ellipse at 30% 25%, var(--card-white) 0%, #efeff0 55%, var(--marble-grey) 100%);
    box-shadow: 0 10px 28px var(--card-shadow);
    overflow: hidden;
  }
  .couple-name {
    position: absolute;
    font-family: "Playfair Display", "Bodoni Moda", serif;
    font-weight: 700;
    color: var(--royal-blue);
    line-height: 1;
    letter-spacing: -4px;
    text-shadow: -5px 4px 0 var(--ink);
  }
  .couple-name--first { left: 84px; top: 100px; font-size: 150px; }
  .couple-name--joiner { left: 268px; top: 232px; font-size: 130px; }
  .couple-name--second { left: 390px; top: 370px; font-size: 150px; }
  .invite-line {
    position: absolute;
    left: 0;
    width: 100%;
    text-align: center;
    font-family: "Cormorant Garamond", serif;
    font-weight: 500;
    color: var(--ink);
  }
  .invite-line--lead { top: 560px; font-size: 44px; }
  .invite-line--place { top: 712px; font-size: 46px; }
  .event-date {
    position: absolute;
    left: 0;
    top: 630px;
    width: 100%;
    display: flex;
    justify-content: center;
    align-items: center;
    gap: 14px;
    font-family: "Bodoni Moda", serif;
    color: var(--ink);
    font-size: 52px;
    line-height: 1;
  }
  .event-date__divider {
    width: 3px;
    height: 64px;
    background: var(--ink);
  }
  .event-date__day sup { font-size: 26px; vertical-align: 18px; }
  .event-date__year { letter-spacing: 22px; margin-right: -22px; }
  .landscape {
    position: absolute;
    left: 0;
    bottom: 0;
    width: 100%;
    height: 290px;
  }
</style>
</head>
<body>
<main class="canvas">
  <article class="invitation">
    <h1 class="couple">
      <span class="couple-name couple-name--first">Tessa</span>
      <span class="couple-name couple-name--joiner">and</span>
      <span class="couple-name couple-name--second">Boyd</span>
    </h1>
    <p class="invite-line invite-line--lead">Invite you to celebrate</p>
    <p class="event-date">
      <span class="event-date__month">October</span>
      <span class="event-date__divider"></span>
      <span class="event-date__day">19<sup>th</sup></span>
      <span class="event-date__divider"></span>
      <span class="event-date__year">2019</span>
    </p>
    <p class="invite-line invite-line--place">Charlotte, NC</p>
    <svg class="landscape" viewBox="0 0 802 290" preserveAspectRatio="none" role="img" aria-label="Black ink illustration of mountain peaks, a fire lookout tower and a pine forest along the bottom of the card">
      <defs>
        <linearGradient id="landscape-tone" x1="0" y1="0" x2="0" y2="1">
          <stop offset="0" stop-color="#8a8a8a"/>
          <stop offset="1" stop-color="#141414"/>
        </linearGradient>
      </defs>
      <rect x="0" y="0" width="802" height="290" fill="url(#landscape-tone)"/>
    </svg>
  </article>
</main>
</body>
</html>
```